Information One Page for Email

I am looking for a informative attachment I can send with an introductive email for Ridgeview Cable Works. Something I can also Mail.

Ridgeview Cable Works is the leader in Rebar Post Tension Cable Placement and Post Tension Cable repair. Outside of cable placement and repair we do concrete repair, Parking Garage restoration and

Content

Post Tension Repair and Concrete Restoration
Post-tensioning is a revolutionary method in concrete construction that enhances the strength and durability of structures. However, like all construction ele-ments, post-tension cables can experience wear and damage over time. Ensuring timely and effective repair is crucial for maintaining the safety and integrity of your building.
Why Post-Tension Cable Repair is Essential
1. **Structural Integrity**: Damaged or deteriorated cables can compromise the structural integrity of your building, leading to safety hazards and potential structural failures.
2. **Extended Lifespan**: Regular maintenance and repair of post-tension cables extend the lifespan of your structure, ensuring it remains safe and function-al for years to come.
3. **Cost-Effective**: Addressing cable issues early on prevents more severe damage and costly repairs down the line.
Common Signs of Post-Tension Cable Issues
- Cracks in concrete surfaces
- Unusual noises or popping sounds
- Visible cable ends or broken strands
- Water leakage through cracks
Our Repair Process
1. **Inspection and Assessment**: Our team conducts a thorough inspection to identify the extent of the damage and determine the appropriate repair meth-ods.
2. **Cable Repair or Replacement**: Depending on the severity, we either re-pair the existing cables or replace them with new ones to restore full functional-ity.
3. **Sealing and Protection**: After repairing, we seal the affected areas to protect against moisture and future damage.
4. **Quality Assurance**: We perform rigorous quality checks to ensure the repairs meet industry standards and the structure is safe for use.
Why Choose Us
- **Expertise and Experience**: With years of experience in post-tension cable repair, our team is skilled in handling even the most complex repairs efficiently and effectively.
- **Advanced Technology**: We use the latest technology and materials to ensure durable and long-lasting repairs.
- **Customer Satisfaction**: Our commitment to quality and customer satisfaction sets us apart. We work closely with our clients to ensure their needs are met and expectations exceeded.
Contact Us
If you suspect issues with your post-tension cables or need a routine inspection, don't hesitate to contact us. Our experts are ready to provide the best solutions to keep your structures safe and secure.
Ensure the safety and longevity of your building with our professional post-tension cable repair services. Trust us to deliver quality and reliability every time.

```html
<!DOCTYPE html>
<html lang="en">
<head>
<meta charset="utf-8">
<title>Ridgeview Cable Works – Post Tension Repair &amp; Concrete Restoration</title>
<link href="https://fonts.googleapis.com/css2?family=Montserrat:wght@600;700;800&family=Open+Sans:wght@400;600;700&display=swap" rel="stylesheet">
<style>
  :root{
    --green:#2f9a5a;
    --green-dark:#217a45;
    --ink:#1d2629;
    --charcoal:#262e31;
    --body:#4a5356;
    --pale:#eef1f0;
    --white:#ffffff;
  }
  *{margin:0;padding:0;box-sizing:border-box}
  html,body{width:870px;height:1200px;overflow:hidden;background:var(--white)}
  body{position:relative;font-family:"Open Sans",Arial,sans-serif;color:var(--body)}
  .heading{font-family:"Montserrat",Arial,sans-serif;color:var(--ink)}

  .hero-photo{position:absolute;top:0;right:0;width:430px;height:430px;
    background:linear-gradient(160deg,#d9dedd 0%,#a9b1b0 45%,#7b8584 100%);
    clip-path:polygon(28% 0,100% 0,100% 100%,0 100%,0 22%)}
  .brand{position:absolute;top:40px;left:42px;display:flex;align-items:center;gap:12px}
  .brand-mark{width:18px;height:18px;background:var(--green)}
  .brand-name{font-family:"Montserrat",Arial,sans-serif;font-weight:700;font-size:22px;color:var(--green-dark);line-height:1.1}

  .lead{position:absolute;top:140px;left:42px;width:385px}
  .title{font-size:28px;font-weight:800;line-height:1.15}
  .title-rule{width:70px;height:5px;background:var(--green);margin:12px 0 12px}
  .intro{width:370px;font-size:13px;line-height:1.55}

  .essential{position:absolute;top:420px;left:42px;width:380px}
  .essential h2{font-size:21px;font-weight:800;line-height:1.2;margin-bottom:16px}
  .essential h2 span{color:var(--green)}
  .benefit{display:flex;gap:14px;margin-bottom:14px}
  .icon{flex:none;width:38px;height:38px;background:var(--green);border-radius:6px;display:flex;align-items:center;justify-content:center}
  .benefit h3{font-family:"Montserrat",Arial,sans-serif;font-size:15px;font-weight:700;color:var(--green-dark);margin-bottom:3px}
  .benefit p{font-size:12.5px;line-height:1.45}

  .signs{position:absolute;top:430px;left:460px;width:390px;height:320px;background:var(--pale)}
  .signs-head{background:var(--green);color:var(--white);font-family:"Montserrat",Arial,sans-serif;font-weight:800;font-size:18px;line-height:1.25;padding:16px 22px;text-transform:uppercase}
  .signs ul{list-style:none;padding:14px 22px}
  .signs li{display:flex;align-items:center;gap:14px;font-size:15px;font-weight:600;color:var(--ink);margin-bottom:12px}
  .signs .icon{width:40px;height:40px}

  .process{position:absolute;top:770px;left:0;width:525px;height:345px;background:var(--charcoal);padding:0 30px 0 42px}
  .process-tab{display:inline-block;background:var(--green);color:var(--white);font-family:"Montserrat",Arial,sans-serif;font-weight:700;font-size:20px;padding:12px 26px;margin:-4px 0 16px -42px;border-radius:0 30px 30px 0}
  .step{display:flex;gap:14px;margin-bottom:12px}
  .step-num{flex:none;width:30px;height:30px;background:var(--green);color:var(--white);font-family:"Montserrat",Arial,sans-serif;font-weight:800;font-size:15px;display:flex;align-items:center;justify-content:center;border-radius:4px}
  .step h3{font-family:"Montserrat",Arial,sans-serif;font-size:15px;font-weight:700;color:var(--white);margin-bottom:2px}
  .step p{font-size:11.5px;line-height:1.4;color:#c4cbcc}

  .choose{position:absolute;top:790px;left:555px;width:300px}
  .choose h2{font-size:28px;font-weight:800;margin-bottom:16px}
  .reason{display:flex;gap:12px;margin-bottom:14px}
  .reason h3{font-family:"Montserrat",Arial,sans-serif;font-size:14.5px;font-weight:700;color:var(--green-dark);margin-bottom:2px}
  .reason p{font-size:11.5px;line-height:1.4}

  .footer{position:absolute;left:0;bottom:0;width:870px;height:85px;background:var(--ink);display:flex;align-items:center;justify-content:space-between;padding:0 42px}
  .footer-note{width:470px;font-size:10.5px;line-height:1.45;color:#c9d0d1}
  .contact{text-align:right}
  .phone{display:flex;align-items:center;gap:8px;font-family:"Montserrat",Arial,sans-serif;font-weight:800;font-size:28px;color:var(--green)}
  .web{font-size:13px;font-weight:600;color:var(--white)}
</style>
</head>
<body>

<div class="hero-photo" role="img" aria-label="Photo of a multi-storey concrete building under post-tension construction"></div>

<div class="brand"><span class="brand-mark"></span><span class="brand-name">Ridgeview Cable Works</span></div>

<div class="lead">
  <h1 class="heading title">Post Tension Repair<br>&amp; Concrete Restoration</h1>
  <div class="title-rule"></div>
  <p class="intro">Post-tensioning is a revolutionary method in concrete construction that enhances the strength and durability of structures. However, like all construction elements, post-tension cables can experience wear and damage over time. Ensuring timely and effective repair is crucial for maintaining the safety and integrity of your building.</p>
</div>

<section class="essential">
  <h2 class="heading">Why <span>Post-Tension Cable</span> Repair is Essential</h2>
  <div class="benefit">
    <div class="icon"><svg width="22" height="22" viewBox="0 0 24 24" fill="none" stroke="#fff" stroke-width="2.2"><path d="M4 20V9l8-5 8 5v11z"/><path d="M9 20v-6h6v6"/></svg></div>
    <div><h3>Structural Integrity</h3><p>Damaged or deteriorated cables can compromise the structural integrity of your building, leading to safety hazards and potential structural failures.</p></div>
  </div>
  <div class="benefit">
    <div class="icon"><svg width="22" height="22" viewBox="0 0 24 24" fill="none" stroke="#fff" stroke-width="2.2"><circle cx="12" cy="12" r="8"/><path d="M12 7v5l3 3"/></svg></div>
    <div><h3>Extended Lifespan</h3><p>Regular maintenance and repair of post-tension cables extend the lifespan of your structure, ensuring it remains safe and functional for years to come.</p></div>
  </div>
  <div class="benefit">
    <div class="icon"><svg width="22" height="22" viewBox="0 0 24 24" fill="none" stroke="#fff" stroke-width="2.2"><path d="M12 3v18"/><path d="M16 7H10a3 3 0 0 0 0 6h4a3 3 0 0 1 0 6H8"/></svg></div>
    <div><h3>Cost-Effective</h3><p>Addressing cable issues early on prevents more severe damage and costly repairs down the line.</p></div>
  </div>
</section>

<section class="signs">
  <div class="signs-head">Common Signs of<br>Post Tension Cable Issues</div>
  <ul>
    <li><span class="icon"><svg width="22" height="22" viewBox="0 0 24 24" fill="none" stroke="#fff" stroke-width="2.2"><path d="M10 3l3 6-4 4 4 8"/></svg></span>Cracks in concrete surfaces</li>
    <li><span class="icon"><svg width="22" height="22" viewBox="0 0 24 24" fill="none" stroke="#fff" stroke-width="2.2"><path d="M4 9h4l5-4v14l-5-4H4z"/><path d="M17 9a4 4 0 0 1 0 6"/></svg></span>Unusual noises or popping sounds</li>
    <li><span class="icon"><svg width="22" height="22" viewBox="0 0 24 24" fill="none" stroke="#fff" stroke-width="2.2"><path d="M3 12h7M14 12h7M10 8l4 8"/></svg></span>Visible cable ends or broken strands</li>
    <li><span class="icon"><svg width="22" height="22" viewBox="0 0 24 24" fill="none" stroke="#fff" stroke-width="2.2"><path d="M12 3c4 5 6 8 6 11a6 6 0 0 1-12 0c0-3 2-6 6-11z"/></svg></span>Water leakage through cracks</li>
  </ul>
</section>

<section class="process">
  <div class="process-tab">Our Repair Process</div>
  <div class="step"><div class="step-num">1</div><div><h3>Inspection and Assessment</h3><p>Our team conducts a thorough inspection to identify the extent of the damage and determine the appropriate repair methods.</p></div></div>
  <div class="step"><div class="step-num">2</div><div><h3>Cable Repair or Replacement</h3><p>Depending on the severity, we either repair the existing cables or replace them with new ones to restore full functionality.</p></div></div>
  <div class="step"><div class="step-num">3</div><div><h3>Sealing and Protection</h3><p>After repairing, we seal the affected areas to protect against moisture and future damage.</p></div></div>
  <div class="step"><div class="step-num">4</div><div><h3>Quality Assurance</h3><p>We perform rigorous quality checks to ensure the repairs meet industry standards and the structure is safe for use.</p></div></div>
</section>

<section class="choose">
  <h2 class="heading">WHY CHOOSE US</h2>
  <div class="reason">
    <div class="icon"><svg width="22" height="22" viewBox="0 0 24 24" fill="none" stroke="#fff" stroke-width="2.2"><circle cx="12" cy="9" r="5"/><path d="M9 13l-2 8 5-3 5 3-2-8"/></svg></div>
    <div><h3>Expertise &amp; Experience</h3><p>With years of experience in post-tension cable repair, our team is skilled in handling even the most complex repairs efficiently and effectively.</p></div>
  </div>
  <div class="reason">
    <div class="icon"><svg width="22" height="22" viewBox="0 0 24 24" fill="none" stroke="#fff" stroke-width="2.2"><circle cx="12" cy="12" r="3"/><path d="M12 3v3M12 18v3M3 12h3M18 12h3M5.6 5.6l2.1 2.1M16.3 16.3l2.1 2.1M5.6 18.4l2.1-2.1M16.3 7.7l2.1-2.1"/></svg></div>
    <div><h3>Advanced Technology</h3><p>We use the latest technology and materials to ensure durable and long-lasting repairs.</p></div>
  </div>
  <div class="reason">
    <div class="icon"><svg width="22" height="22" viewBox="0 0 24 24" fill="none" stroke="#fff" stroke-width="2.4"><path d="M5 12l5 5 9-10"/></svg></div>
    <div><h3>Customer Satisfaction</h3><p>Our commitment to quality and customer satisfaction sets us apart.</p></div>
  </div>
</section>

<footer class="footer">
  <p class="footer-note">If you suspect issues with your post-tension cables or need a routine inspection, don't hesitate to contact us. Our experts are ready to provide the best solutions to keep your structures safe and secure.</p>
  <div class="contact">
    <div class="phone"><svg width="24" height="24" viewBox="0 0 24 24" fill="#2f9a5a"><path d="M6.6 10.8a15 15 0 0 0 6.6 6.6l2.2-2.2a1 1 0 0 1 1-.25 11.4 11.4 0 0 0 3.6.57 1 1 0 0 1 1 1V20a1 1 0 0 1-1 1A17 17 0 0 1 3 4a1 1 0 0 1 1-1h3.5a1 1 0 0 1 1 1c0 1.25.2 2.45.57 3.57a1 1 0 0 1-.25 1z"/></svg>555-013-4829</div>
    <div class="web">www.ridgeviewcableworks.com</div>
  </div>
</footer>

</body>
</html>
```